Design a few pages of a luxury magazine for the Prestige Aubergerie Lyon

We need a luxury design for our magazine. See the inDesign pages of the current version attached (zip).

Please work primarily on the first double page (Inventez le luxe de demain) that contains only one photo with legend, a title and the text both in French and English. It must be made clear that the text is the same in two different languages (it is not clear enough here).

You can also work on the other two double pages selected. Feedback will be provided and the 10 best pages will be submitted to a vote at the end of the project timespan.

The most important is a classy and luxury design, this will be printed on expensive paper.

See the full brochure here: https://www.prestigeaubergerie.com/brochure/#page=4

Target Market(s)

Students and parents

Industry/Entity Type

Education

Colors

Designer to choose colors to be used in the design.

Requirements
Must have
• Luxury magazine layout, see:
• https://www.findwerk.com/search?q=luxury+magazine+layout&client=safari&rls=en&source=lnms&tbm=isch&sa=X&ved=0ahUKEwitoIDmit7fAhUVShUIHXC2Cd4Q_AUIDigB&biw=1010&bih=702
Nice to have
• The color of the cover that should be used for blue and grey is #393d49.
• Our font for serif titles (from the logo) is Adobe TRAJAN.
Should not have
• flashy colors

```html
<!DOCTYPE html>
<html lang="fr">
<head>
<meta charset="utf-8">
<title>Prestige Aubergerie Lyon — Inventez le luxe de demain</title>
<link rel="stylesheet" href="https://fonts.googleapis.com/css2?family=Playfair+Display:wght@700&family=Cormorant+Garamond:wght@300;400&family=Arimo:wght@400&display=swap">
<style>
  :root {
    --backdrop: #e3e3e3;
    --page-white: #ffffff;
    --band-grey: #eef0f1;
    --page-black: #121212;
    --page-black-soft: #2a2a2a;
    --ink-light: #f2f2f2;
    --ink-body: #d9d9d9;
    --photo-warm: #b88a55;
    --photo-dark: #2b2620;
  }
  * { margin: 0; padding: 0; box-sizing: border-box; }
  html, body {
    width: 1200px; height: 1200px; overflow: hidden;
    background: var(--backdrop);
  }
  .spread {
    position: absolute;
    left: 50px; top: 240px;
    width: 1100px; height: 720px;
    display: flex;
    box-shadow: 0 18px 40px rgba(0,0,0,0.18);
  }
  .page { position: relative; width: 550px; height: 720px; overflow: hidden; }

  .page--photo { background: var(--page-white); }
  .page--photo .band {
    position: absolute; left: 0; right: 0; top: 120px; height: 470px;
    background: var(--band-grey);
  }
  .page--photo .photo {
    position: absolute; left: 40px; top: 220px; width: 420px; height: 270px;
    background: linear-gradient(160deg, var(--photo-dark) 0%, #6b5435 40%, var(--photo-warm) 75%, #d8b07a 100%);
  }

  .page--text {
    background: radial-gradient(ellipse at 55% 45%, var(--page-black-soft) 0%, var(--page-black) 60%);
    color: var(--ink-light);
  }
  .title { line-height: 1; }
  .title__main {
    display: block;
    font-family: "Playfair Display", serif; font-weight: 700; font-size: 30px;
  }
  .title__sub {
    display: block;
    font-family: "Cormorant Garamond", serif; font-weight: 300; font-size: 27px;
    margin-top: 2px;
  }
  .lang-fr { position: absolute; left: 36px; top: 46px; width: 330px; }
  .lang-en { position: absolute; right: 34px; top: 330px; width: 470px; text-align: right; }
  .body-copy {
    font-family: "Arimo", sans-serif; font-size: 9px; line-height: 1.55;
    color: var(--ink-body); text-align: justify; margin-top: 16px;
  }
  .lang-en .body-copy { text-align: justify; text-align-last: right; }
  .body-copy p + p { margin-top: 8px; }
</style>
</head>
<body>
  <main class="spread">
    <section class="page page--photo">
      <div class="band"></div>
      <div class="photo" role="img" aria-label="Photo de groupe de quatre membres de l'équipe en tenue de soirée autour d'une méridienne verte dans un salon d'hôtel de luxe"></div>
    </section>

    <section class="page page--text">
      <article class="lang-fr" lang="fr">
        <h2 class="title">
          <span class="title__main">Inventez</span>
          <span class="title__sub">le luxe de demain</span>
        </h2>
        <div class="body-copy">
          <p>Depuis sa création il y a 30 ans, notre école garde le même objectif : que chaque étudiant acquière les compétences et développe les talents essentiels pour briller dans l'univers du luxe. Première école dédiée à l'hôtellerie de luxe, Prestige Aubergerie délivre un Bachelor et un Master of Science in International Tourism and Hospitality Management, deux grades universitaires anglais. Cette combinaison du luxe à la française et du management anglo-saxon donne toutes les clés à nos étudiants pour s'assurer une place privilégiée dans l'univers du luxe en France et à l'international. Grâce à l'excellence académique de nos programmes, la dimension internationale de nos formations et l'immersion professionnelle à travers des stages dans les plus prestigieux hôtels du monde, tous nos diplômés sont assurés de faire carrière dans le secteur de leur choix à un poste stratégique. La moitié d'entre eux signent un CDI avant même la fin de leur dernier stage.</p>
        </div>
      </article>

      <article class="lang-en" lang="en">
        <h2 class="title">
          <span class="title__main">Invent</span>
          <span class="title__sub">the luxury of tommorow</span>
        </h2>
        <div class="body-copy">
          <p>Since its foundation 30 years ago, our school has had only one objective: that each student acquires the skills and develops the essential talents they require to shine within the luxury sector. Prestige Aubergerie is the first Higher Education establishment dedicated to luxury hotel training: we offer a Bachelor's and a Master's degree in International Tourism and Hospitality Management. This combination of French-style luxury and Anglo-Saxon management gives our students the key elements they need to ensure a privileged position within the luxury industry both in France and internationally. The academic excellence of our programmes, the international dimension of our training and</p>
          <p>our professional work placements at the most prestigious hotels in the world all ensure that our graduates are certain to secure a career in a strategic role in the luxury sector. Half of our students sign a permanent contract before they even finish their final work placement.</p>
        </div>
      </article>
    </section>
  </main>
</body>
</html>
```